529 aim Higher

Redesigning this front and back business card flyer and keeping the info but making it look better.

This is all about using the info and logo on the business card design and creating a better layout using any of the following and more.

Changing the background color or imagine, chaining the placement of content, resizing content.

Target Market(s)

Targeting people that have been injured on one side and people that have been giving a DUI on the other.

Contact Information for Business Card

We are looking to keep the info but make it look a fee cleaner and less cluttered

Font styles to use
Sans Serif

Requirements
Must have
• Must have the same info but a better layout.
Nice to have
• better background colors or image or layout. different fonts or same font all design options that will make it look professional and clean.

```html
<!DOCTYPE html>
<html lang="en">
<head>
<meta charset="utf-8">
<title>529 aim Higher – Card Concept</title>
<link rel="stylesheet" href="https://fonts.googleapis.com/css2?family=Montserrat:wght@400;500;600;700;800;900&display=swap">
<style>
  :root {
    --red: #c8161b;
    --red-dark: #8e0c0f;
    --black: #111111;
    --white: #ffffff;
    --board: #e3e3e3;
    --label: #8a8a8a;
  }
  * { box-sizing: border-box; margin: 0; padding: 0; }
  html, body { width: 1200px; height: 1099px; overflow: hidden; }
  body {
    background: var(--board);
    font-family: "Montserrat", Arial, sans-serif;
    position: relative;
  }
  .card {
    position: absolute;
    top: 152px;
    width: 448px;
    height: 746px;
    overflow: hidden;
    box-shadow: 4px 6px 10px rgba(0,0,0,.25);
  }
  .card--front { left: 125px; background: var(--black); }
  .card--back { left: 627px; background: var(--white); }
  .card__shapes { position: absolute; inset: 0; }
  .abs { position: absolute; left: 0; width: 100%; text-align: center; }

  .brand {
    position: absolute; left: 0; width: 100%;
    display: flex; align-items: center; justify-content: center; gap: 12px;
  }
  .brand__mark { width: 36px; height: 36px; background: var(--red); }
  .brand__name { font-weight: 800; font-size: 40px; letter-spacing: -0.5px; line-height: 1; }
  .card--front .brand { top: 38px; }
  .card--front .brand__name { color: var(--white); }
  .card--back .brand { top: 582px; }
  .card--back .brand__name { color: var(--black); }

  .front__intro { top: 112px; color: var(--white); font-size: 28px; font-weight: 400; letter-spacing: -0.3px; }
  .front__headline { top: 142px; color: var(--red); font-size: 54px; font-weight: 900; letter-spacing: -1px; line-height: 60px; }

  .reasons { position: absolute; list-style: none; }
  .reasons li { display: flex; align-items: flex-start; gap: 10px; }
  .reasons svg { flex: none; width: 16px; height: 16px; margin-top: 4px; }
  .front__reasons { left: 42px; top: 196px; color: var(--white); font-size: 21px; line-height: 24.8px; }
  .back__reasons { left: 33px; top: 287px; color: var(--black); font-size: 19.5px; line-height: 25px; width: 410px; }

  .photo-circle {
    position: absolute; border-radius: 50%;
    border: 4px solid var(--red);
    box-shadow: 0 5px 10px rgba(0,0,0,.4);
  }
  .photo-circle--wheelchair { left: 190px; top: 437px; width: 127px; height: 127px;
    background:
      radial-gradient(ellipse 30% 60% at 50% 50%, rgba(20,24,30,.85), rgba(20,24,30,0) 100%),
      linear-gradient(90deg, #2b3036 0%, #7f8c98 25%, #b9c6d1 45%, #8c99a5 60%, #3a4048 85%, #22262b 100%); }
  .photo-circle--boot { left: 330px; top: 428px; width: 86px; height: 86px;
    background:
      radial-gradient(ellipse 30% 55% at 45% 45%, rgba(30,32,36,.9), rgba(30,32,36,0) 100%),
      linear-gradient(180deg, #8f8a84 0%, #b7b0a8 55%, #cfc8c0 100%); }

  .front__tagline { top: 573px; color: var(--black); font-size: 25px; font-weight: 600; line-height: 29px; }

  .contact { top: 680px; color: var(--white); }
  .contact__phone { font-size: 25px; font-weight: 800; line-height: 28px; letter-spacing: .3px; }
  .contact__web { font-size: 24px; font-weight: 400; line-height: 28px; }

  .back__title { top: 28px; color: var(--white); font-size: 50px; font-weight: 900; line-height: 47px; letter-spacing: -0.5px; }
  .back__question { top: 131px; color: var(--white); font-size: 20px; font-weight: 700; line-height: 29px; letter-spacing: .4px; }

  .side-label {
    position: absolute; color: var(--label); font-size: 24px; font-weight: 400;
    letter-spacing: 1px; transform: rotate(-90deg); transform-origin: left top;
  }
  .side-label--front { left: 77px; top: 890px; }
  .side-label--back { left: 1107px; top: 900px; }
  .board-caption { position: absolute; top: 991px; left: 0; width: 100%; text-align: center; color: var(--label); font-size: 26px; font-weight: 500; }
</style>
</head>
<body>

<section class="card card--front" aria-label="Card front">
  <svg class="card__shapes" viewBox="0 0 448 746" width="448" height="746">
    <defs>
      <linearGradient id="sceneBase" x1="0" y1="0" x2="0" y2="1">
        <stop offset="0" stop-color="#111111"/>
        <stop offset="0.12" stop-color="#1c241d"/>
        <stop offset="0.28" stop-color="#2f3a30"/>
        <stop offset="0.36" stop-color="#8d9195"/>
        <stop offset="0.5" stop-color="#5d6166"/>
        <stop offset="1" stop-color="#2a2c30"/>
      </linearGradient>
      <radialGradient id="silverTone" cx="0.5" cy="0.5" r="0.5">
        <stop offset="0" stop-color="#c9ccd0" stop-opacity="0.95"/>
        <stop offset="0.55" stop-color="#7b8087" stop-opacity="0.7"/>
        <stop offset="1" stop-color="#3a3d42" stop-opacity="0"/>
      </radialGradient>
      <radialGradient id="darkTone" cx="0.5" cy="0.5" r="0.5">
        <stop offset="0" stop-color="#0d0f12" stop-opacity="0.95"/>
        <stop offset="0.6" stop-color="#1c1f24" stop-opacity="0.7"/>
        <stop offset="1" stop-color="#1c1f24" stop-opacity="0"/>
      </radialGradient>
      <radialGradient id="glintTone" cx="0.5" cy="0.5" r="0.5">
        <stop offset="0" stop-color="#e4e7ea" stop-opacity="0.7"/>
        <stop offset="1" stop-color="#e4e7ea" stop-opacity="0"/>
      </radialGradient>
      <linearGradient id="fadeTop" x1="0" y1="0" x2="0" y2="1">
        <stop offset="0" stop-color="#111111"/>
        <stop offset="1" stop-color="#111111" stop-opacity="0"/>
      </linearGradient>
      <clipPath id="sceneClip"><path d="M0,250 H448 V440 Q230,520 0,455 Z"/></clipPath>
      <linearGradient id="stopTone" x1="0" y1="0" x2="1" y2="1">
        <stop offset="0" stop-color="#b01216"/>
        <stop offset="1" stop-color="#7a0a0c"/>
      </linearGradient>
    </defs>
    <rect x="0" y="455" width="448" height="291" fill="#ffffff"/>
    <g role="img" aria-label="Photo of a wrecked silver pickup and a damaged black sedan after a road collision" clip-path="url(#sceneClip)">
      <rect x="0" y="250" width="448" height="280" fill="url(#sceneBase)"/>
      <ellipse cx="150" cy="400" rx="170" ry="95" fill="url(#silverTone)"/>
      <ellipse cx="340" cy="420" rx="150" ry="85" fill="url(#darkTone)"/>
      <ellipse cx="380" cy="370" rx="70" ry="30" fill="url(#glintTone)"/>
      <ellipse cx="120" cy="355" rx="90" ry="25" fill="url(#glintTone)"/>
      <ellipse cx="100" cy="470" rx="140" ry="45" fill="url(#darkTone)"/>
      <rect x="0" y="250" width="448" height="60" fill="url(#fadeTop)"/>
    </g>
    <path d="M0,455 Q230,520 448,440 L448,446 Q230,528 0,462 Z" fill="#ffffff"/>
    <path d="M0,462 Q230,528 448,446 L448,452 Q230,560 0,478 Z" fill="#111111"/>
    <path d="M0,465 Q230,525 448,447" stroke="#c8161b" stroke-width="2" fill="none"/>
    <path d="M0,746 V690 Q224,612 448,690 V746 Z" fill="#111111"/>
    <path d="M0,746 V705 Q224,625 448,705 V746 Z" fill="#c8161b"/>
  </svg>

  <div class="brand"><span class="brand__mark"></span><span class="brand__name">529 aim Higher</span></div>
  <p class="abs front__intro">IF YOU’VE BEEN INJURED</p>
  <h1 class="abs front__headline">AIM HIGHER</h1>
  <ul class="reasons front__reasons">
    <li><svg viewBox="0 0 16 16"><circle cx="8" cy="8" r="6.5" fill="none" stroke="#c8161b" stroke-width="2"/><line x1="3.5" y1="12.5" x2="12.5" y2="3.5" stroke="#c8161b" stroke-width="2"/></svg>for an inexperienced lawyer!</li>
    <li><svg viewBox="0 0 16 16"><circle cx="8" cy="8" r="6.5" fill="none" stroke="#c8161b" stroke-width="2"/><line x1="3.5" y1="12.5" x2="12.5" y2="3.5" stroke="#c8161b" stroke-width="2"/></svg>for less than you deserve!</li>
    <li><svg viewBox="0 0 16 16"><circle cx="8" cy="8" r="6.5" fill="none" stroke="#c8161b" stroke-width="2"/><line x1="3.5" y1="12.5" x2="12.5" y2="3.5" stroke="#c8161b" stroke-width="2"/></svg>for paying massive medical bills!</li>
    <li><svg viewBox="0 0 16 16"><circle cx="8" cy="8" r="6.5" fill="none" stroke="#c8161b" stroke-width="2"/><line x1="3.5" y1="12.5" x2="12.5" y2="3.5" stroke="#c8161b" stroke-width="2"/></svg>for a life of pain and debt!</li>
  </ul>

  <div class="photo-circle photo-circle--wheelchair" role="img" aria-label="Photo of a person in a wheelchair by a bright window"></div>
  <div class="photo-circle photo-circle--boot" role="img" aria-label="Photo of a leg in a medical walking boot"></div>

  <p class="abs front__tagline">We fight for you, so you<br>can focus on getting better</p>
  <div class="abs contact">
    <p class="contact__phone">CALL 529-555-0147</p>
    <p class="contact__web">www.529AimHigher.com</p>
  </div>
</section>

<section class="card card--back" aria-label="Card back">
  <svg class="card__shapes" viewBox="0 0 448 746" width="448" height="746">
    <defs>
      <linearGradient id="headerTone" x1="0" y1="0" x2="1" y2="1">
        <stop offset="0" stop-color="#b01216"/>
        <stop offset="0.6" stop-color="#c8161b"/>
        <stop offset="1" stop-color="#7a0a0c"/>
      </linearGradient>
      <radialGradient id="headerShade" cx="0.5" cy="0.5" r="0.5">
        <stop offset="0" stop-color="#5e0608" stop-opacity="0.6"/>
        <stop offset="1" stop-color="#5e0608" stop-opacity="0"/>
      </radialGradient>
      <radialGradient id="headerLight" cx="0.5" cy="0.5" r="0.5">
        <stop offset="0" stop-color="#e0474b" stop-opacity="0.55"/>
        <stop offset="1" stop-color="#e0474b" stop-opacity="0"/>
      </radialGradient>
      <clipPath id="headerClip"><path d="M0,0 H448 V180 Q240,280 0,198 Z"/></clipPath>
    </defs>
    <g role="img" aria-label="Red-toned photo of a driver handing over documents at a traffic stop" clip-path="url(#headerClip)">
      <rect x="0" y="0" width="448" height="260" fill="url(#headerTone)"/>
      <ellipse cx="90" cy="140" rx="120" ry="90" fill="url(#headerShade)"/>
      <ellipse cx="380" cy="60" rx="110" ry="70" fill="url(#headerShade)"/>
      <ellipse cx="250" cy="90" rx="120" ry="60" fill="url(#headerLight)"/>
      <ellipse cx="180" cy="220" rx="140" ry="50" fill="url(#headerShade)"/>
    </g>
    <path d="M0,198 Q240,280 448,180 L448,184 Q240,330 0,212 Z" fill="#111111"/>
    <path d="M0,746 V690 Q224,612 448,690 V746 Z" fill="#c8161b"/>
    <path d="M0,746 V705 Q224,625 448,705 V746 Z" fill="#111111"/>
  </svg>

  <h2 class="abs back__title">AIM HIGHER<br>AFTER A DUI</h2>
  <p class="abs back__question">WHAT SHOULD I DO IF<br>I GET PULLED OVER FOR DUI?</p>

  <ul class="reasons back__reasons">
    <li><svg viewBox="0 0 16 16"><circle cx="8" cy="8" r="6.5" fill="none" stroke="#c8161b" stroke-width="2"/><line x1="3.5" y1="12.5" x2="12.5" y2="3.5" stroke="#c8161b" stroke-width="2"/></svg>Pull over in a calm, normal manner</li>
    <li><svg viewBox="0 0 16 16"><circle cx="8" cy="8" r="6.5" fill="none" stroke="#c8161b" stroke-width="2"/><line x1="3.5" y1="12.5" x2="12.5" y2="3.5" stroke="#c8161b" stroke-width="2"/></svg>Be polite at all times</li>
    <li><svg viewBox="0 0 16 16"><circle cx="8" cy="8" r="6.5" fill="none" stroke="#c8161b" stroke-width="2"/><line x1="3.5" y1="12.5" x2="12.5" y2="3.5" stroke="#c8161b" stroke-width="2"/></svg>Do not admit to drinking</li>
    <li><svg viewBox="0 0 16 16"><circle cx="8" cy="8" r="6.5" fill="none" stroke="#c8161b" stroke-width="2"/><line x1="3.5" y1="12.5" x2="12.5" y2="3.5" stroke="#c8161b" stroke-width="2"/></svg><span>Do not submit to any field<br>sobriety tests</span></li>
    <li><svg viewBox="0 0 16 16"><circle cx="8" cy="8" r="6.5" fill="none" stroke="#c8161b" stroke-width="2"/><line x1="3.5" y1="12.5" x2="12.5" y2="3.5" stroke="#c8161b" stroke-width="2"/></svg><span>Do not submit to talking a chemical<br>test (breath, blood, or urine)</span></li>
    <li><svg viewBox="0 0 16 16"><circle cx="8" cy="8" r="6.5" fill="none" stroke="#c8161b" stroke-width="2"/><line x1="3.5" y1="12.5" x2="12.5" y2="3.5" stroke="#c8161b" stroke-width="2"/></svg><span>Do not make any statement after<br>being arrested, especially when<br>placed in the police cruiser</span></li>
  </ul>

  <div class="brand"><span class="brand__mark"></span><span class="brand__name">529 aim Higher</span></div>

  <div class="abs contact">
    <p class="contact__phone">CALL 529-555-0147</p>
    <p class="contact__web">www.529AimHigher.com</p>
  </div>
</section>

<span class="side-label side-label--front">FRONT</span>
<span class="side-label side-label--back">BACK</span>
<p class="board-caption">Design Concept 529 aim Higher 1</p>

</body>
</html>
```